Speisekarten für ein modernes, junges Café
Zielgruppe
Wir suchen eine Speisekarte für ein modernes, junges Café. Frühstück, kleine Speisen, Snacks und Getränke stehen auf der Karte. Unsere Zielgruppe sind hauptsächlich junge Menschen bis 40 Jahre.
Die Speisekarte sollte immer änderbar sein ( nur Text bei neuen Speisen zum Beispiel )
Aufgabenstellung
Das Logo kann und soll gerne mit eingefügt werden. Eventuell gleich auf dem Deckblatt.
Generell bin ich offen für junge, coole Ideen.
Unten die Themen/ grobe Überschriften
Kaffee und Espresso
Frühstücksvariationen
Eierspeisen
Frühstück zum löffeln
Pancakes
Extras zum Frühstück
Snacks/ kleine Speisen
-die Kurbel. Drinks
-die Kurbel. Wein & Bier )
((Kinderspeisekarte:
zusätzlich noch ein extra Blatt für die Kinder zum ausmalen mit den illustrierten Bildern auch im modernen Stil ))

```html
<!DOCTYPE html>
<html lang="en">
<head>
<meta charset="utf-8">
<title>die Kurbel. – Menu</title>
<link rel="stylesheet" href="https://fonts.googleapis.com/css2?family=Amaranth:wght@700&family=Poppins:wght@400;600;700;800&display=swap">
<style>
:root{
  --bg:#c6c6c6;
  --ink:#2a2324;
  --tan:#b8a78a;
  --sand:#ede2d2;
  --paper:#ffffff;
  --dark:#231f20;
}
*{box-sizing:border-box;margin:0;padding:0}
html,body{width:1200px;height:1117px;overflow:hidden;background:var(--bg)}
body{position:relative;font-family:"Poppins",sans-serif;color:var(--ink)}
.page{position:absolute;top:180px;width:536px;height:757px;background:var(--paper);box-shadow:6px 8px 14px rgba(0,0,0,.25);overflow:hidden}
.page--front{left:54px}
.page--kids{left:611px}
.page__top{position:absolute;left:0;top:0;width:100%;height:190px;background:var(--dark)}
.page__bottom{position:absolute;left:0;bottom:0;width:100%;height:199px;background:var(--tan)}
.page__sheet{position:absolute;left:10px;right:10px;top:11px;bottom:10px;background:var(--paper)}
.page__frame{position:absolute;left:17px;right:17px;top:17px;bottom:17px;border:2.5px solid var(--tan)}
.hero{position:absolute;left:25px;top:24px;width:486px;height:180px}
.logo{position:absolute;left:190px;top:-2px;width:156px;height:156px;border-radius:50%;background:var(--dark);border:7px solid var(--paper);display:flex;align-items:center;justify-content:center}
.logo__name{font-family:"Amaranth",sans-serif;font-weight:700;font-size:24px;color:var(--paper)}
.section{position:absolute;width:200px}
.section__label{display:block;width:170px;height:19px;background:var(--sand);border-radius:3px;font-family:"Amaranth",sans-serif;font-weight:700;font-size:14.5px;line-height:19px;text-align:center;color:var(--ink)}
.items{list-style:none}
.item{height:22.6px}
.item__name{display:block;font-weight:700;font-size:11.3px;line-height:12px}
.item__desc{display:block;font-size:7px;line-height:10px;white-space:nowrap;width:198px;overflow:hidden}
.rule{position:absolute;height:1.5px;width:193px;background:var(--ink)}
.extras{position:absolute;left:284px;top:500px;width:207px;height:59px;border:2px solid var(--tan);border-radius:8px;text-align:center;padding-top:11px}
.extras__title{font-family:"Amaranth",sans-serif;font-weight:700;font-size:19px;line-height:20px}
.extras__sub{font-weight:600;font-size:9.5px;line-height:13px}
.drinks{position:absolute;left:43px;top:580px;width:448px;height:143px;border:2px solid var(--dark);border-radius:10px}
.drinks__divider{position:absolute;left:222px;top:12px;width:1px;height:116px;background:var(--tan)}
.drinks__col{position:absolute;top:12px;width:200px}
.drinks__title{font-family:"Amaranth",sans-serif;font-weight:700;font-size:21px;line-height:24px;margin-bottom:4px}
.kids-menu{position:absolute;left:39px;top:31px;width:459px;height:162px;border:2px solid var(--dark);border-radius:10px}
.kids-menu__title{position:absolute;left:12px;top:11px;width:432px;height:28px;background:var(--sand);border-radius:4px;font-family:"Amaranth",sans-serif;font-weight:700;font-size:20px;line-height:28px;text-align:center}
.kids-menu__col{position:absolute;top:50px;width:200px}
.coloring{position:absolute;left:45px;top:225px;width:453px;height:489px;border-radius:12px;background:radial-gradient(ellipse at 55% 55%,#f4f1ec 0%,#e9e4dc 70%,#f7f5f1 100%)}
.coloring__title{position:absolute;left:100px;top:-4px;font-family:"Poppins",sans-serif;font-weight:800;font-size:44px;line-height:46px;color:var(--dark);letter-spacing:1px}
.coloring__sub{position:absolute;left:135px;top:42px;font-weight:800;font-size:20px;color:var(--tan);letter-spacing:.5px}
</style>
</head>
<body>

<section class="page page--front">
  <div class="page__top"></div>
  <div class="page__bottom"></div>
  <div class="page__sheet"></div>
  <div class="page__frame"></div>

  <svg class="hero" viewBox="0 0 486 180">
    <defs>
      <linearGradient id="photoBreakfast" x1="0" y1="0" x2="1" y2="1">
        <stop offset="0" stop-color="#3a2b22"/><stop offset=".5" stop-color="#7a6a45"/><stop offset="1" stop-color="#4a3426"/>
      </linearGradient>
      <linearGradient id="photoCoffee" x1="0" y1="0" x2="1" y2="1">
        <stop offset="0" stop-color="#eceae6"/><stop offset=".5" stop-color="#d8b58a"/><stop offset="1" stop-color="#f2efea"/>
      </linearGradient>
      <linearGradient id="waveTan" x1="0" x2="1">
        <stop offset="0" stop-color="#d8ccb6"/><stop offset=".5" stop-color="#f1e9dc"/><stop offset="1" stop-color="#b8a78a"/>
      </linearGradient>
    </defs>
    <rect x="0" y="0" width="241" height="160" fill="url(#photoBreakfast)" role="img" aria-label="Photo: avocado toast with fried egg in a pan"/>
    <rect x="244" y="0" width="242" height="160" fill="url(#photoCoffee)" role="img" aria-label="Photo: cappuccino with croissants"/>
    <path d="M0 125 C80 90 160 110 240 135 C320 160 400 155 486 130 L486 180 L0 180 Z" fill="url(#waveTan)"/>
    <path d="M0 148 C80 112 170 128 250 150 C330 172 410 172 486 150 L486 180 L0 180 Z" fill="#ffffff"/>
  </svg>

  <div class="logo"><span class="logo__name">die Kurbel.</span></div>

  <div class="section" style="left:53px;top:226px">
    <span class="section__label">Coffee and espresso</span>
    <ul class="items" style="margin-top:3px">
      <li class="item"><span class="item__name">Lorem ipsum</span><span class="item__desc">Lorem ipsum dolor sit amet, consectetur adipiscing elit,</span></li>
      <li class="item"><span class="item__name">Lorem ipsum</span><span class="item__desc">Lorem ipsum dolor sit amet, consectetur adipiscing elit,</span></li>
      <li class="item"><span class="item__name">Lorem ipsum</span><span class="item__desc">Lorem ipsum dolor sit amet, consectetur adipiscing elit,</span></li>
      <li class="item"><span class="item__name">Lorem ipsum</span><span class="item__desc">Lorem ipsum dolor sit amet, consectetur adipiscing elit,</span></li>
    </ul>
  </div>
  <div class="rule" style="left:53px;top:349px"></div>

  <div class="section" style="left:284px;top:226px">
    <span class="section__label">Breakfast variations</span>
    <ul class="items" style="margin-top:3px">
      <li class="item"><span class="item__name">Lorem ipsum</span><span class="item__desc">Lorem ipsum dolor sit amet, consectetur adipiscing elit,</span></li>
      <li class="item"><span class="item__name">Lorem ipsum</span><span class="item__desc">Lorem ipsum dolor sit amet, consectetur adipiscing elit,</span></li>
      <li class="item"><span class="item__name">Lorem ipsum</span><span class="item__desc">Lorem ipsum dolor sit amet, consectetur adipiscing elit,</span></li>
      <li class="item"><span class="item__name">Lorem ipsum</span><span class="item__desc">Lorem ipsum dolor sit amet, consectetur adipiscing elit,</span></li>
    </ul>
  </div>
  <div class="rule" style="left:284px;top:349px"></div>

  <div class="section" style="left:53px;top:361px">
    <span class="section__label">Egg dishes</span>
    <ul class="items" style="margin-top:3px">
      <li class="item"><span class="item__name">Lorem ipsum</span><span class="item__desc">Lorem ipsum dolor sit amet, consectetur adipiscing elit,</span></li>
      <li class="item"><span class="item__name">Lorem ipsum</span><span class="item__desc">Lorem ipsum dolor sit amet, consectetur adipiscing elit,</span></li>
      <li class="item"><span class="item__name">Lorem ipsum</span><span class="item__desc">Lorem ipsum dolor sit amet, consectetur adipiscing elit,</span></li>
    </ul>
  </div>
  <div class="rule" style="left:53px;top:461px"></div>

  <div class="section" style="left:284px;top:362px">
    <span class="section__label">Breakfast to eat</span>
    <ul class="items" style="margin-top:9px">
      <li class="item"><span class="item__name">Lorem ipsum</span><span class="item__desc">Lorem ipsum dolor sit amet, consectetur adipiscing elit,</span></li>
      <li class="item"><span class="item__name">Lorem ipsum</span><span class="item__desc">Lorem ipsum dolor sit amet, consectetur adipiscing elit,</span></li>
      <li class="item"><span class="item__name">Lorem ipsum</span><span class="item__desc">Lorem ipsum dolor sit amet, consectetur adipiscing elit,</span></li>
      <li class="item"><span class="item__name">Lorem ipsum</span><span class="item__desc">Lorem ipsum dolor sit amet, consectetur adipiscing elit,</span></li>
    </ul>
  </div>

  <div class="section" style="left:53px;top:473px">
    <span class="section__label">Pancakes</span>
    <ul class="items" style="margin-top:3px">
      <li class="item"><span class="item__name">Lorem ipsum</span><span class="item__desc">Lorem ipsum dolor sit amet, consectetur adipiscing elit,</span></li>
      <li class="item"><span class="item__name">Lorem ipsum</span><span class="item__desc">Lorem ipsum dolor sit amet, consectetur adipiscing elit,</span></li>
      <li class="item"><span class="item__name">Lorem ipsum</span><span class="item__desc">Lorem ipsum dolor sit amet, consectetur adipiscing elit,</span></li>
    </ul>
  </div>

  <div class="extras">
    <div class="extras__title">Extras for breakfast</div>
    <div class="extras__sub">Snacks/small dishes</div>
  </div>

  <div class="drinks">
    <div class="drinks__col" style="left:13px">
      <div class="drinks__title">Drinks</div>
      <ul class="items">
        <li class="item"><span class="item__name">Lorem ipsum</span><span class="item__desc">Lorem ipsum dolor sit amet, consectetur adipiscing elit,</span></li>
        <li class="item"><span class="item__name">Lorem ipsum</span><span class="item__desc">Lorem ipsum dolor sit amet, consectetur adipiscing elit,</span></li>
        <li class="item"><span class="item__name">Lorem ipsum</span><span class="item__desc">Lorem ipsum dolor sit amet, consectetur adipiscing elit,</span></li>
        <li class="item"><span class="item__name">Lorem ipsum</span><span class="item__desc">Lorem ipsum dolor sit amet, consectetur adipiscing elit,</span></li>
      </ul>
    </div>
    <div class="drinks__divider"></div>
    <div class="drinks__col" style="left:237px">
      <div class="drinks__title">Wine &amp; Beer</div>
      <ul class="items">
        <li class="item"><span class="item__name">Lorem ipsum</span><span class="item__desc">Lorem ipsum dolor sit amet, consectetur adipiscing elit,</span></li>
        <li class="item"><span class="item__name">Lorem ipsum</span><span class="item__desc">Lorem ipsum dolor sit amet, consectetur adipiscing elit,</span></li>
        <li class="item"><span class="item__name">Lorem ipsum</span><span class="item__desc">Lorem ipsum dolor sit amet, consectetur adipiscing elit,</span></li>
        <li class="item"><span class="item__name">Lorem ipsum</span><span class="item__desc">Lorem ipsum dolor sit amet, consectetur adipiscing elit,</span></li>
      </ul>
    </div>
  </div>
</section>

<section class="page page--kids">
  <div class="page__top"></div>
  <div class="page__bottom"></div>
  <div class="page__sheet"></div>
  <div class="page__frame"></div>

  <div class="kids-menu">
    <div class="kids-menu__title">Children's menu:</div>
    <ul class="items kids-menu__col" style="left:13px">
      <li class="item"><span class="item__name">Lorem ipsum</span><span class="item__desc">Lorem ipsum dolor sit amet, consectetur adipiscing elit,</span></li>
      <li class="item"><span class="item__name">Lorem ipsum</span><span class="item__desc">Lorem ipsum dolor sit amet, consectetur adipiscing elit,</span></li>
      <li class="item"><span class="item__name">Lorem ipsum</span><span class="item__desc">Lorem ipsum dolor sit amet, consectetur adipiscing elit,</span></li>
      <li class="item"><span class="item__name">Lorem ipsum</span><span class="item__desc">Lorem ipsum dolor sit amet, consectetur adipiscing elit,</span></li>
    </ul>
    <ul class="items kids-menu__col" style="left:246px">
      <li class="item"><span class="item__name">Lorem ipsum</span><span class="item__desc">Lorem ipsum dolor sit amet, consectetur adipiscing elit,</span></li>
      <li class="item"><span class="item__name">Lorem ipsum</span><span class="item__desc">Lorem ipsum dolor sit amet, consectetur adipiscing elit,</span></li>
      <li class="item"><span class="item__name">Lorem ipsum</span><span class="item__desc">Lorem ipsum dolor sit amet, consectetur adipiscing elit,</span></li>
      <li class="item"><span class="item__name">Lorem ipsum</span><span class="item__desc">Lorem ipsum dolor sit amet, consectetur adipiscing elit,</span></li>
    </ul>
  </div>

  <div class="coloring" role="img" aria-label="Colouring illustration: outline drawing of a pineapple, popsicle, apple, strawberry cake and stars">
    <span class="coloring__title">HAPPY</span>
    <span class="coloring__sub">COLORING</span>
  </div>
</section>

</body>
</html>
```